Photographic Tutorial website

We are looking for a fresh design for a photographic tutorial / workshop website. The website will have the included functions:

* Home (needs to have a login section)
* About Us
* Info about each course / workshop.
* Subscribe to courses and pay online.
* Members Area
* Photo gallery
* Contact us

The website will be implemented with our own made cms. We do not need it to be coded. We have a team ready to do this for us. We only need the PSD layout.

We have attached a mockup design that the client and I have come up with and we need the design to be taken to the next level.

Client also likes:
http://www.lumavistacamera.example/

Requirements
Must have
• Must Stand out i.e black backgrounds
Should not have
• Alter the logo in anyway.

```html
<!DOCTYPE html>
<html lang="en">
<head>
<meta charset="utf-8">
<title>Bright Aperture – Photographic Tuition</title>
<link href="https://fonts.googleapis.com/css2?family=Cinzel:wght@400;700&family=Merriweather:wght@700&family=Open+Sans:ital,wght@0,300;0,400;0,600;1,400&display=swap" rel="stylesheet">
<style>
:root{
  --bg:#151515;
  --text:#8a8a8a;
  --white:#ffffff;
  --brown:#a8743a;
  --pink:#b8447f;
  --green:#2f8f2a;
  --orange:#c2431c;
  --red:#b3121b;
  --yellow:#e5d92a;
  --coral:#e0573a;
  --lime:#6bbf2a;
  --cyan:#2fb4d8;
  --magenta:#d64ba4;
  --phone:#7cbf2a;
  --blue-link:#4aa3d8;
  --serif:'Cinzel', serif;
  --display:'Merriweather', serif;
  --sans:'Open Sans', sans-serif;
}
*{box-sizing:border-box;margin:0;padding:0}
html,body{width:1200px;height:2595px;overflow:hidden}
body{background:var(--bg);font-family:var(--sans);color:var(--text);position:relative}
.abs{position:absolute}

.site-header{position:absolute;left:0;top:0;width:1200px;height:120px;background:linear-gradient(#0d0d0d,#1b1b1b)}
.header-scene{position:absolute;left:560px;top:0;width:480px;height:120px;background:radial-gradient(ellipse at 50% 95%,#c98a3c 0%,#5a4a5a 35%,#1b1f2a 70%,#101010 100%)}
.brand{position:absolute;left:143px;top:34px;display:flex;align-items:center;gap:10px}
.brand-dot{width:28px;height:28px;border-radius:50%;background:var(--red)}
.brand-name{font-family:var(--sans);font-weight:600;font-size:30px;color:var(--white);line-height:1}
.brand-tag{position:absolute;left:181px;top:70px;font-family:var(--serif);font-size:11px;letter-spacing:3px;color:#ccc}
.login{position:absolute;right:140px;top:16px;font-family:var(--serif);font-size:12px;color:var(--lime);letter-spacing:1px;display:flex;align-items:center;gap:6px}
.call-label{position:absolute;right:142px;top:60px;font-family:var(--serif);font-size:12px;color:#ccc;letter-spacing:1px}
.call-phone{position:absolute;right:140px;top:76px;font-size:26px;color:var(--white);font-weight:300}

.main-nav{position:absolute;left:0;top:120px;width:1200px;height:30px;background:linear-gradient(90deg,#d73a8c 0%,#e0433a 15%,#e9a82a 32%,#d9d22b 42%,#57b438 58%,#2fb0b0 72%,#3b6fd0 85%,#8a4bc8 100%)}
.main-nav ul{list-style:none;display:flex;justify-content:space-between;margin:0 140px 0 148px;height:30px;align-items:center}
.main-nav li{font-family:var(--serif);font-weight:700;font-size:13px;color:#1a1a1a}
.main-nav li.current{color:var(--white)}

.hero-band{position:absolute;left:0;top:150px;width:1200px;height:470px;background:linear-gradient(#3a3a3a,#232323 60%,#181818)}
.hero-frame{position:absolute;left:143px;top:175px;width:912px;height:420px;border:6px solid #0e0e0e;border-radius:4px;box-shadow:0 8px 20px rgba(0,0,0,.7);overflow:hidden}
.hero-photo{position:absolute;inset:0;background:linear-gradient(#6e93b8 0%,#a7b8c4 18%,#8b5a34 30%,#a7683a 55%,#6f6a3c 75%,#4a4a2a 100%)}
.hero-title{position:absolute;left:0;right:0;top:215px;text-align:center;font-family:var(--display);font-size:54px;color:var(--white);text-shadow:0 2px 6px rgba(0,0,0,.6)}
.hero-caption{position:absolute;left:20px;right:20px;top:302px;height:86px;background:rgba(40,40,40,.75);padding:14px 18px;font-size:21px;font-weight:300;line-height:30px;color:#ddd;text-transform:uppercase}
.hero-arrow{position:absolute;top:365px;width:38px;height:38px;border-radius:50%;background:#d8d8d8;border:2px solid #888;display:flex;align-items:center;justify-content:center}

.feature{position:absolute;top:651px;width:166px}
.feature-pic{height:130px;border:4px solid}
.feature h3{font-family:var(--serif);font-size:13px;font-weight:400;text-align:center;margin-top:12px;line-height:17px;text-transform:uppercase}
.feature p{font-size:10.5px;line-height:15px;text-align:center;margin-top:4px;color:#7a7a7a}

.section-bar{position:absolute;left:143px;width:667px;height:30px;display:flex;justify-content:space-between;align-items:center;padding:0 14px;font-family:var(--serif);font-weight:700;font-size:15px;color:var(--white)}
.section-bar small{font-family:var(--sans);font-weight:400;font-size:12px}
.post{position:absolute;left:143px;width:667px;height:190px}
.post-date{position:absolute;left:0;top:0;width:40px;height:42px;font-family:var(--serif);font-size:10px;line-height:13px;color:var(--white);text-align:center;padding-top:5px}
.post-title{position:absolute;left:58px;top:8px;font-size:19px;font-weight:400;color:var(--white)}
.post-thumb{position:absolute;left:0;top:58px;width:108px;height:108px;border:4px solid #3a3a3a}
.post-text{position:absolute;left:128px;top:52px;width:520px;font-size:11.5px;line-height:20px;color:#6a6a6a}
.post-meta{position:absolute;left:128px;top:156px;display:flex;gap:26px;font-size:10px;font-style:italic;color:#666;align-items:center}
.post-meta span{display:flex;align-items:center;gap:7px}
.divider{position:absolute;left:830px;top:930px;width:0;height:1320px;border-left:1px dashed #333}

.moon-banner{position:absolute;left:850px;top:930px;width:208px;height:82px;border-radius:3px;background:linear-gradient(#2d58c8,#0f1f6a 70%,#0a1230);border:2px solid #3a3a3a}
.side-title{position:absolute;left:840px;width:230px;text-align:center;font-family:var(--serif);font-size:11.5px;line-height:18px;color:#ccc;white-space:nowrap}
.calendar{position:absolute;left:850px;top:1085px;width:210px;height:232px;background:#3a3a3a;padding:6px}
.cal-head{height:22px;display:flex;justify-content:space-between;align-items:center;color:#ddd;font-size:11px;padding:0 8px}
.cal-grid{display:grid;grid-template-columns:repeat(7,1fr);gap:3px;margin-top:4px}
.cal-grid span{height:25px;display:flex;align-items:center;justify-content:center;font-size:12px;color:#ddd;background:#262626}
.cal-grid span.dow{height:14px;font-size:8px;background:none;color:#ccc}
.cal-grid span.off{color:#666}
.cal-grid span.today{background:var(--red);color:#fff}
.side-bar{position:absolute;left:850px;width:210px;height:30px;padding:0 12px;font-family:var(--serif);font-weight:700;font-size:11.5px;color:var(--white);display:flex;align-items:center;white-space:nowrap}
.check-list{position:absolute;left:856px;top:1382px;list-style:none}
.check-list li{display:flex;align-items:center;gap:12px;font-family:var(--serif);font-weight:700;font-size:11px;color:#ddd;height:34px;white-space:nowrap}
.gallery{position:absolute;left:850px;top:1552px;width:212px;display:grid;grid-template-columns:repeat(3,64px);gap:9px}
.gallery div{height:64px;border:3px solid #555}
.testimonial{position:absolute;left:856px;top:1955px;width:196px;height:190px;background:#2a2a2a;padding:12px 14px;font-size:10.5px;font-style:italic;line-height:16px;color:#7a7a7a;overflow:hidden}
.testimonial-name{position:absolute;left:856px;top:2170px;width:196px;text-align:right;font-size:11px;font-style:italic;color:var(--blue-link)}

.site-footer{position:absolute;left:0;top:2270px;width:1200px;height:325px;background:linear-gradient(#242424,#151515);border-top:3px solid #5a0f16}
.footer-contact{position:absolute;left:147px;top:30px;font-size:12px;color:#ccc}
.footer-contact .lead{font-family:var(--serif);font-size:13px;line-height:20px;color:var(--white)}
.footer-contact .phone{font-size:30px;color:var(--phone);font-weight:300;margin:2px 0 14px}
.footer-contact p{line-height:20px}
.footer-contact a{color:var(--blue-link);text-decoration:none}
.footer-courses{position:absolute;left:523px;top:28px;width:260px}
.footer-courses h4{font-family:var(--serif);font-size:17px;color:var(--blue-link);font-weight:400;margin-bottom:14px}
.footer-courses li{list-style:none;font-size:12px;line-height:18px;color:#aaa;padding:7px 0;border-bottom:1px dotted #3a3a3a}
.partner{position:absolute;left:905px;width:150px;height:32px;border-radius:4px;background:#353535}
.copyright{position:absolute;left:150px;top:290px;font-size:10px;color:#555}
.copyright em{color:var(--coral);font-style:normal}
.social{position:absolute;top:284px;width:22px;height:22px;border-radius:3px;background:#4a4a4a}
</style>
</head>
<body>

<header class="site-header">
  <div class="header-scene" role="img" aria-label="Photographer silhouette at sunset"></div>
  <div class="brand"><span class="brand-dot"></span><span class="brand-name">Bright Aperture</span></div>
  <div class="brand-tag">PHOTOGRAPHIC TUITION</div>
  <div class="login">LOGIN
    <svg width="12" height="12" viewBox="0 0 12 12"><circle cx="6" cy="6" r="5" fill="none" stroke="#6bbf2a" stroke-width="1.5"/><path d="M5 3.5 7.5 6 5 8.5" fill="none" stroke="#6bbf2a" stroke-width="1.5"/></svg>
  </div>
  <div class="call-label">CALL US ON</div>
  <div class="call-phone">0400 555 017</div>
</header>

<nav class="main-nav">
  <ul>
    <li class="current">HOME</li><li>ABOUT US</li><li>COURSE / WORKSHOP</li><li>SUBSCRIBE &amp; PAY ONLINE</li><li>MEMBERS AREA</li><li>PHOTO GALLERY</li><li>CONTACT US</li>
  </ul>
</nav>

<section class="hero-band"></section>
<div class="hero-frame">
  <div class="hero-photo" role="img" aria-label="Canyon landscape with red cliffs under a blue sky"></div>
  <div class="hero-title">“Neque porro quisquam est”</div>
  <div class="hero-caption">Lorem Ipsum is simply dummy text of the printing &amp; typesetting industry. Lorem Ipsum has been the industry's standard...</div>
</div>
<div class="hero-arrow" style="left:124px"><svg width="14" height="14" viewBox="0 0 14 14"><path d="M9 2 4 7l5 5" fill="none" stroke="#444" stroke-width="2.5"/></svg></div>
<div class="hero-arrow" style="left:1036px"><svg width="14" height="14" viewBox="0 0 14 14"><path d="M5 2l5 5-5 5" fill="none" stroke="#444" stroke-width="2.5"/></svg></div>

<div class="feature" style="left:143px">
  <div class="feature-pic" style="border-color:var(--yellow);background:linear-gradient(#5aa6e0,#bcd8ef 55%,#8a6a3a)" role="img" aria-label="Wooden pier under a blue sky"></div>
  <h3 style="color:var(--yellow)">Urdan Excursion</h3>
  <p>Lorem Ipsum is simply dummy text of the printing &amp; typesetting industry. Lorem Ipsum has been the industry's standard dummy text ever since the 1500...</p>
</div>
<div class="feature" style="left:331px">
  <div class="feature-pic" style="border-color:var(--coral);background:linear-gradient(#6aa8d8,#c8d8e0 45%,#b06a4a 60%,#2f7fa0)" role="img" aria-label="Waterfront huts panorama"></div>
  <h3 style="color:var(--coral)">Panorama</h3>
  <p>Lorem Ipsum is simply dummy text of the printing &amp; typesetting industry. Lorem Ipsum has been the industry's standard dummy text ever since the 1500...</p>
</div>
<div class="feature" style="left:519px">
  <div class="feature-pic" style="border-color:var(--lime);background:linear-gradient(#1a2a5a,#3a3a7a 50%,#c88a2a 75%,#2a1a1a)" role="img" aria-label="City lights at night"></div>
  <h3 style="color:var(--lime)">Night Photography<br>&amp; City Lights</h3>
  <p>Lorem Ipsum is simply dummy text of the printing &amp; typesetting industry. Lorem Ipsum has been the industry's standard...</p>
</div>
<div class="feature" style="left:705px">
  <div class="feature-pic" style="border-color:var(--cyan);background:linear-gradient(135deg,#2a5a8a,#8ab8d8 50%,#3a4a5a)" role="img" aria-label="Glass office towers"></div>
  <h3 style="color:var(--cyan)">City Walks</h3>
  <p>Lorem Ipsum is simply dummy text of the printing &amp; typesetting industry. Lorem Ipsum has been the industry's standard dummy text ever since the 1500...</p>
</div>
<div class="feature" style="left:893px">
  <div class="feature-pic" style="border-color:var(--magenta);background:linear-gradient(#4a7ac8,#d8d0c0 50%,#b82a2a 75%,#2a6a2a)" role="img" aria-label="Domed building with red flowers in HDR"></div>
  <h3 style="color:var(--magenta)">HDR</h3>
  <p>Lorem Ipsum is simply dummy text of the printing &amp; typesetting industry. Lorem Ipsum has been the industry's standard dummy text ever since the 1500...</p>
</div>

<div class="section-bar" style="top:932px;background:var(--brown)">GENERAL INFORMATION &amp; BA's 2012<small>Read all »</small></div>

<article class="post" style="top:980px">
  <div class="post-date" style="background:var(--brown)">JUN 10<br>2012</div>
  <h2 class="post-title">Donec vulputate nulla in nibh pellentesque consequat.</h2>
  <div class="post-thumb" style="background:linear-gradient(135deg,#c8762a,#3a2a1a)" role="img" aria-label="Tiger resting"></div>
  <p class="post-text">Lorem ipsum dolor sit amet, consectetuer adipiscing elit. Donec semper risus id neque vulp elementum. Ut diam neque, vestibulum non, sagittis quis, commodo id, purus. Vivamus sagittis, odio non rhoncus adipiscing, elit ipsum pulvinar est, vitae malesuada velit orci sed arcu...</p>
  <div class="post-meta"><span><svg width="13" height="13" viewBox="0 0 13 13"><circle cx="6.5" cy="6.5" r="5.5" fill="none" stroke="#777"/><path d="M6.5 3v4h3" fill="none" stroke="#777"/></svg>June 10, 2011</span><span><svg width="13" height="12" viewBox="0 0 13 12"><path d="M1 1h11v7H5l-3 3V8H1z" fill="none" stroke="#777"/></svg>No Comments</span></div>
</article>
<article class="post" style="top:1183px">
  <div class="post-date" style="background:var(--brown)">JUN 10<br>2012</div>
  <h2 class="post-title">Donec vulputate nulla in nibh pellentesque consequat.</h2>
  <div class="post-thumb" style="background:linear-gradient(135deg,#c8762a,#3a2a1a)" role="img" aria-label="Tiger resting"></div>
  <p class="post-text">Lorem ipsum dolor sit amet, consectetuer adipiscing elit. Donec semper risus id neque vulp elementum. Ut diam neque, vestibulum non, sagittis quis, commodo id, purus. Vivamus sagittis, odio non rhoncus adipiscing, elit ipsum pulvinar est, vitae malesuada velit orci sed arcu...</p>
  <div class="post-meta"><span><svg width="13" height="13" viewBox="0 0 13 13"><circle cx="6.5" cy="6.5" r="5.5" fill="none" stroke="#777"/><path d="M6.5 3v4h3" fill="none" stroke="#777"/></svg>June 10, 2011</span><span><svg width="13" height="12" viewBox="0 0 13 12"><path d="M1 1h11v7H5l-3 3V8H1z" fill="none" stroke="#777"/></svg>No Comments</span></div>
</article>
<article class="post" style="top:1386px">
  <div class="post-date" style="background:var(--brown)">JUN 10<br>2012</div>
  <h2 class="post-title">Donec vulputate nulla in nibh pellentesque consequat.</h2>
  <div class="post-thumb" style="background:linear-gradient(135deg,#c8762a,#3a2a1a)" role="img" aria-label="Tiger resting"></div>
  <p class="post-text">Lorem ipsum dolor sit amet, consectetuer adipiscing elit. Donec semper risus id neque vulp elementum. Ut diam neque, vestibulum non, sagittis quis, commodo id, purus. Vivamus sagittis, odio non rhoncus adipiscing, elit ipsum pulvinar est, vitae malesuada velit orci sed arcu...</p>
  <div class="post-meta"><span><svg width="13" height="13" viewBox="0 0 13 13"><circle cx="6.5" cy="6.5" r="5.5" fill="none" stroke="#777"/><path d="M6.5 3v4h3" fill="none" stroke="#777"/></svg>June 10, 2011</span><span><svg width="13" height="12" viewBox="0 0 13 12"><path d="M1 1h11v7H5l-3 3V8H1z" fill="none" stroke="#777"/></svg>No Comments</span></div>
</article>

<div class="section-bar" style="top:1590px;background:var(--pink)">USA FALL TRAVEL TOUR<small>Read all »</small></div>

<article class="post" style="top:1640px">
  <div class="post-date" style="background:var(--pink)">JUN 10<br>2012</div>
  <h2 class="post-title">Donec vulputate nulla in nibh pellentesque consequat.</h2>
  <div class="post-thumb" style="background:linear-gradient(#8ab0d0,#5a8a3a 55%,#2a4a1a)" role="img" aria-label="Green mountain valley"></div>
  <p class="post-text">Lorem ipsum dolor sit amet, consectetuer adipiscing elit. Donec semper risus id neque vulp elementum. Ut diam neque, vestibulum non, sagittis quis, commodo id, purus. Vivamus sagittis, odio non rhoncus adipiscing, elit ipsum pulvinar est, vitae malesuada velit orci sed arcu...</p>
  <div class="post-meta"><span><svg width="13" height="13" viewBox="0 0 13 13"><circle cx="6.5" cy="6.5" r="5.5" fill="none" stroke="#777"/><path d="M6.5 3v4h3" fill="none" stroke="#777"/></svg>June 10, 2011</span><span><svg width="13" height="12" viewBox="0 0 13 12"><path d="M1 1h11v7H5l-3 3V8H1z" fill="none" stroke="#777"/></svg>No Comments</span></div>
</article>
<article class="post" style="top:1843px">
  <div class="post-date" style="background:var(--pink)">JUN 10<br>2012</div>
  <h2 class="post-title">Donec vulputate nulla in nibh pellentesque consequat.</h2>
  <div class="post-thumb" style="background:linear-gradient(#8ab0d0,#5a8a3a 55%,#2a4a1a)" role="img" aria-label="Green mountain valley"></div>
  <p class="post-text">Lorem ipsum dolor sit amet, consectetuer adipiscing elit. Donec semper risus id neque vulp elementum. Ut diam neque, vestibulum non, sagittis quis, commodo id, purus. Vivamus sagittis, odio non rhoncus adipiscing, elit ipsum pulvinar est, vitae malesuada velit orci sed arcu...</p>
  <div class="post-meta"><span><svg width="13" height="13" viewBox="0 0 13 13"><circle cx="6.5" cy="6.5" r="5.5" fill="none" stroke="#777"/><path d="M6.5 3v4h3" fill="none" stroke="#777"/></svg>June 10, 2011</span><span><svg width="13" height="12" viewBox="0 0 13 12"><path d="M1 1h11v7H5l-3 3V8H1z" fill="none" stroke="#777"/></svg>No Comments</span></div>
</article>
<article class="post" style="top:2046px">
  <div class="post-date" style="background:var(--pink)">JUN 10<br>2012</div>
  <h2 class="post-title">Donec vulputate nulla in nibh pellentesque consequat.</h2>
  <div class="post-thumb" style="background:linear-gradient(#8ab0d0,#5a8a3a 55%,#2a4a1a)" role="img" aria-label="Green mountain valley"></div>
  <p class="post-text">Lorem ipsum dolor sit amet, consectetuer adipiscing elit. Donec semper risus id neque vulp elementum. Ut diam neque, vestibulum non, sagittis quis, commodo id, purus. Vivamus sagittis, odio non rhoncus adipiscing, elit ipsum pulvinar est, vitae malesuada velit orci sed arcu...</p>
  <div class="post-meta"><span><svg width="13" height="13" viewBox="0 0 13 13"><circle cx="6.5" cy="6.5" r="5.5" fill="none" stroke="#777"/><path d="M6.5 3v4h3" fill="none" stroke="#777"/></svg>June 10, 2011</span><span><svg width="13" height="12" viewBox="0 0 13 12"><path d="M1 1h11v7H5l-3 3V8H1z" fill="none" stroke="#777"/></svg>No Comments</span></div>
</article>

<div class="divider"></div>

<div class="moon-banner" role="img" aria-label="Moon phase chart banner with crescent moon and clouds"></div>
<div class="side-title" style="top:1045px">Daily Shooting Times Nautical<br>Twilight Start to End</div>
<div class="calendar">
  <div class="cal-head"><span>◂</span><span>July 2012</span><span>▸</span></div>
  <div class="cal-grid">
    <span class="dow">MON</span><span class="dow">TUE</span><span class="dow">WED</span><span class="dow">THU</span><span class="dow">FRI</span><span class="dow">SAT</span><span class="dow">SUN</span>
    <span class="off">25</span><span class="off">26</span><span class="off">27</span><span class="off">28</span><span class="off">29</span><span class="off">30</span><span>1</span>
    <span>2</span><span>3</span><span>4</span><span>5</span><span>6</span><span>7</span><span>8</span>
    <span>9</span><span>10</span><span>11</span><span>12</span><span>13</span><span>14</span><span>15</span>
    <span>16</span><span>17</span><span>18</span><span>19</span><span>20</span><span>21</span><span class="today">22</span>
    <span>23</span><span>24</span><span>25</span><span>26</span><span>27</span><span>28</span><span>29</span>
    <span>30</span><span>31</span>
  </div>
</div>

<div class="side-bar" style="top:1345px;background:var(--green)">Photograpers Check Lists</div>
<ul class="check-list">
  <li><svg width="20" height="18" viewBox="0 0 20 18"><path d="M2 2h16v10H8l-4 4v-4H2z" fill="none" stroke="#aaa" stroke-width="1.5"/></svg>Wedding Shoot Check list</li>
  <li><svg width="20" height="18" viewBox="0 0 20 18"><path d="M2 2h16v10H8l-4 4v-4H2z" fill="none" stroke="#aaa" stroke-width="1.5"/></svg>Pre Shoot Check list</li>
  <li><svg width="20" height="18" viewBox="0 0 20 18"><path d="M2 2h16v10H8l-4 4v-4H2z" fill="none" stroke="#aaa" stroke-width="1.5"/></svg>Standard Check list</li>
</ul>

<div class="side-bar" style="top:1505px;background:var(--orange)">Members Gallery</div>
<div class="gallery" role="img" aria-label="Grid of member photographs">
  <div style="background:linear-gradient(#9ac060,#e0e8c0)"></div>
  <div style="background:linear-gradient(#3a6ac8,#c86a2a)"></div>
  <div style="background:linear-gradient(#d8d8d8,#6a6a6a)"></div>
  <div style="background:linear-gradient(#e8b020,#8a5a10)"></div>
  <div style="background:linear-gradient(#2a3a9a,#c89a5a)"></div>
  <div style="background:linear-gradient(#b8c8e0,#5a6a7a)"></div>
  <div style="background:linear-gradient(#7a6a8a,#d88a4a 60%,#2a2a2a)"></div>
  <div style="background:linear-gradient(#4a8ad8,#e8e8e8)"></div>
  <div style="background:linear-gradient(#d81a2a,#5a0a0a)"></div>
  <div style="background:linear-gradient(#9ac060,#e0e8c0)"></div>
  <div style="background:linear-gradient(#3a6ac8,#c86a2a)"></div>
  <div style="background:linear-gradient(#d8d8d8,#6a6a6a)"></div>
  <div style="background:linear-gradient(#e8b020,#8a5a10)"></div>
  <div style="background:linear-gradient(#2a3a9a,#c89a5a)"></div>
  <div style="background:linear-gradient(#b8c8e0,#5a6a7a)"></div>
</div>

<div class="side-title" style="top:1925px;text-align:left;left:850px;width:210px">Testimonials</div>
<blockquote class="testimonial">Lorem ipsum dolor sit consectetuer adipiscing elit. Donec semper risus id neque vulp elementum. Ut diam neque, estium non, sagittis quis, commissmus sagittis, odio non rhoncus adiping, elit ipsum pulvinar est, vitae malesuada velit orci sed arcu. Lorem ipsum dolor sit consectetuer adipiscing elit. Donec semper risus id neque vudeit rhoncus adiping elit ipsum...</blockquote>
<svg class="abs" style="left:880px;top:2145px" width="20" height="14" viewBox="0 0 20 14"><path d="M0 0h20L4 14z" fill="#2a2a2a"/></svg>
<div class="testimonial-name">- Daniel Reeve</div>

<footer class="site-footer">
  <div class="footer-contact">
    <div class="lead">FOR MORE INFO ABOUT OUR COURSES,<br>PLEASE CONTACT</div>
    <div class="phone">0400 555 017</div>
    <p>17 Harbour Lane, Suite 4,<br>NSW 2000, Australia,<br>FAX: 02 5550 1234</p>
    <p>Email: <a href="#">info@brightaperture.example</a></p>
  </div>
  <div class="footer-courses">
    <h4>OUR COURSES</h4>
    <ul>
      <li>Night Photography</li>
      <li>Leaqrning the basics of Exposure, Aventure, ISO &amp; compesition</li>
      <li>Learning your camera funcations</li>
      <li>How to pick that good spot</li>
      <li>What equipment do I need</li>
    </ul>
  </div>
  <div class="partner" style="top:36px"></div>
  <div class="partner" style="top:86px"></div>
  <div class="partner" style="top:136px"></div>
  <div class="partner" style="top:186px"></div>
  <div class="copyright">Copyright © 2012 Bright Aperture. All Rights Reserved. <em>Links &amp; Reviews</em></div>
  <div class="social" style="left:965px"></div>
  <div class="social" style="left:995px"></div>
  <div class="social" style="left:1025px"></div>
</footer>

</body>
</html>
```